professional business card

A Clean looking business card for a money transfer company. Our company is call Velorix= Transfer + Send = Transcend (next level)
to show professionalism as well as some effects to show digital tech.

1 side to have position, name and address
2 side to have company name and show that we provide money exchange and cross-border money transfer

Target Market(s)

Remittance companies and high net worth individuals

Industry/Entity Type

Finance

Contact Information for Business Card

Name, address, email, title, services- money exchange and cross-border remittance

Requirements
Nice to have
• Digital age feel

```html
<!DOCTYPE html>
<html lang="en">
<head>
<meta charset="utf-8">
<title>Velorix Business Card</title>
<link href="https://fonts.googleapis.com/css2?family=Montserrat:wght@400;500;700&display=swap" rel="stylesheet">
<style>
  :root {
    --navy: #293642;
    --cyan: #6fcbdb;
    --white: #ffffff;
    --ink: #231f20;
    --text: #3a3a3a;
    --shadow-light: #e8e8e8;
    --shadow-dark: #d4d4d4;
  }
  html, body {
    margin: 0;
    padding: 0;
    overflow: hidden;
    background: var(--white);
  }
  .canvas {
    position: relative;
    width: 969px;
    height: 1200px;
    overflow: hidden;
    background: var(--white);
    font-family: "Montserrat", sans-serif;
  }
  .shapes {
    position: absolute;
    inset: 0;
  }
  .brand {
    position: absolute;
    display: flex;
    flex-direction: column;
    align-items: center;
    transform: translateX(-50%);
  }
  .brand-dot {
    width: 56px;
    height: 56px;
    border-radius: 50%;
    background: var(--cyan);
    margin-bottom: 20px;
  }
  .brand-name {
    font-weight: 500;
    font-size: 57px;
    line-height: 1;
    letter-spacing: 1px;
  }
  .brand--front { left: 485px; top: 190px; }
  .brand--front .brand-name { color: var(--white); }
  .brand--back { left: 722px; top: 812px; }
  .brand--back .brand-name { color: var(--navy); }

  .holder {
    position: absolute;
    left: 90px;
    top: 770px;
  }
  .holder-name {
    margin: 0;
    font-weight: 700;
    font-size: 39px;
    letter-spacing: -1px;
    color: var(--ink);
    line-height: 1;
  }
  .holder-position {
    margin: 8px 0 0;
    font-weight: 500;
    font-size: 22px;
    color: var(--ink);
    line-height: 1.2;
  }
  .holder-rule {
    width: 83px;
    height: 3px;
    background: var(--ink);
    margin-top: 12px;
  }
  .contact {
    position: absolute;
    left: 90px;
    top: 915px;
    margin: 0;
    display: grid;
    grid-template-columns: 114px auto;
    row-gap: 8px;
    font-size: 19.5px;
    line-height: 23px;
    color: var(--text);
  }
  .contact dt, .contact dd { margin: 0; }
</style>
</head>
<body>
<div class="canvas">
  <svg class="shapes" width="969" height="1200" viewBox="0 0 969 1200" aria-hidden="true">
    <defs>
      <clipPath id="front-clip">
        <rect x="0" y="0" width="969" height="506" rx="50"/>
      </clipPath>
      <clipPath id="back-clip">
        <rect x="0" y="648" width="969" height="520" rx="50"/>
      </clipPath>
    </defs>

    <!-- front card -->
    <g clip-path="url(#front-clip)">
      <rect class="card-front" x="0" y="0" width="969" height="506" fill="var(--navy)"/>
      <circle cx="485" cy="532" r="62" fill="var(--cyan)"/>
    </g>
    <path d="M111 554 V560 Q160 534 210 534 H755 Q805 534 854 554 Z" fill="var(--shadow-light)"/>

    <!-- back card -->
    <g clip-path="url(#back-clip)">
      <rect x="0" y="648" width="969" height="520" fill="var(--navy)"/>
      <circle cx="485" cy="1194" r="62" fill="var(--cyan)"/>
    </g>
    <rect class="card-back" x="0" y="655" width="969" height="465" rx="50" fill="var(--white)"/>
    <path d="M111 1200 Q160 1180 210 1180 H755 Q805 1180 854 1200 Z" fill="var(--shadow-dark)"/>
  </svg>

  <div class="brand brand--front">
    <div class="brand-dot"></div>
    <div class="brand-name">VELORIX</div>
  </div>

  <div class="holder">
    <h1 class="holder-name">YOUR NAME</h1>
    <p class="holder-position">Your Position</p>
    <div class="holder-rule"></div>
  </div>

  <dl class="contact">
    <dt>Phone</dt><dd>: ++000 0000 000</dd>
    <dt>Location</dt><dd>: Included your city name,</dd>
    <dt>Website</dt><dd>: include your website</dd>
    <dt>Email</dt><dd>: include your email</dd>
  </dl>

  <div class="brand brand--back">
    <div class="brand-dot"></div>
    <div class="brand-name">VELORIX</div>
  </div>
</div>
</body>
</html>
```